Business Consulting Company requires a website design (PSD+HTML+CSS required)

Marlowe Advisory is a Business Consulting Company that provides Analysis, Business Coaching and Systems and Document Design for clients.

We would like a simplistic yet professional looking website design that uses high quality imagery to project a professional persona across our entire site.

The completed project will need to include PSD files (for editing in Photoshop) and will need to also include HTML+CSS coded files that can be edited in Adobe Dreamweaver CS5.5.

Marlowe Advisory currently has a functioning website (located at www.marloweadvisory-example.com.au) but would like to replace its current site with something more professional, user friendly and content simplistic, with the overall design of this project being clean and very easy to navigate whilst remaining professionally focused.

A brief has been attached to this project to provide the key details but please feel free to contact me if you require any clarification or have any questions regarding the project.

Target Market(s)

The target audience for this website will be small to medium sized businesses (of all descriptions).

Industry/Entity Type

Business

Coding

Coded - Design and coding required

Number of Pages Required

5+ page

Requirements
Must have
• Simplistic design structure
• Professional images
• Easy to navigate
• Must be uploaded in PSD format
• Must be coded (HTML+CSS) and compatible with Adobe Dreamweaver CS5.5
Nice to have
• Use of the Company’s corporate colours throughout the site design
• Adding a Home page slider bar with images and short catchy messages (i.e. text based statements)
• Having a quick link box on each page that provides easy navigation throughout the site
• The use of different icons and images to depict our different services (i.e. a different icon and image for analysis service and coaching service etc.).
• All pages should follow a similar theme (universal approach to all pages)
Should not have
• When coding, images should not be used in place of text (all text must be editable)

```html
<!DOCTYPE html>
<html lang="en">
<head>
<meta charset="utf-8">
<title>Marlowe Advisory — Home</title>
<link href="https://fonts.googleapis.com/css2?family=Signika:wght@400;600&family=Open+Sans:wght@400&family=Arimo:ital,wght@0,400;1,400&display=swap" rel="stylesheet">
<style>
:root{
  --blue:#3a8fd6;
  --blue-band:#3e92d8;
  --blue-box:#3584c9;
  --ink:#333;
  --grey:#6b6b6b;
  --line:#dcdcdc;
  --hero-dark:#0b1422;
  --footer:#1a1a1a;
  --white:#fff;
}
*{margin:0;padding:0;box-sizing:border-box}
html,body{width:932px;height:1200px;overflow:hidden;background:var(--white)}
body{position:relative;font-family:'Arimo',Arial,sans-serif;color:var(--ink)}
.abs{position:absolute}

/* header */
.top-rule{left:0;top:0;width:932px;height:3px;background:var(--blue)}
.header{left:0;top:3px;width:932px;height:98px;background:var(--white)}
.brand{left:102px;top:36px;display:flex;align-items:center;gap:10px}
.brand-mark{width:34px;height:34px;border-radius:50%;background:var(--blue)}
.brand-name{font-family:'Signika',sans-serif;font-weight:400;font-size:26px;color:#555;letter-spacing:1px}
.phone{left:725px;top:13px;display:flex;align-items:center;gap:8px;font-family:'Open Sans',sans-serif;font-size:12px;color:#444}
.nav{left:458px;top:56px;display:flex;gap:0;font-family:'Open Sans',sans-serif;font-size:10.5px;color:#333}
.nav a{color:inherit;text-decoration:none;position:absolute;white-space:nowrap}
.nav a.active{color:var(--blue)}

/* hero */
.hero{left:0;top:101px;width:932px;height:405px;background:linear-gradient(90deg,var(--hero-dark) 0%,#13213a 45%,#2c3f5c 70%,#1a2638 100%)}
.hero-photo{left:380px;top:0;width:552px;height:405px;background:radial-gradient(ellipse at 60% 50%,#6f7f96 0%,#34445c 45%,rgba(19,33,58,0) 80%)}
.hero-text{left:110px;font-family:'Signika',sans-serif;font-weight:600;font-size:32px;letter-spacing:.5px;line-height:1}
.hero-text.l1{top:137px;color:var(--blue)}
.hero-text.l2{top:194px;color:var(--white)}
.hero-text.l3{top:250px;color:var(--white)}
.hero-arrow{top:183px}

/* services */
.section-title{left:102px;top:529px;display:flex;align-items:center;gap:12px;font-family:'Signika',sans-serif;font-weight:600;font-size:19px;color:#444}
.section-title span{color:var(--blue)}
.card{top:604px;width:174px;height:294px;border:1px solid var(--line);background:var(--white)}
.card-icon{left:57px;top:-29px;width:58px;height:58px;border-radius:50%;background:var(--white);border:1px solid var(--line);display:flex;align-items:center;justify-content:center}
.card-photo{left:12px;top:38px;width:150px;height:108px;box-shadow:0 2px 4px rgba(0,0,0,.25);border:2px solid var(--white)}
.card-title{left:10px;top:161px;width:156px;font-family:'Signika',sans-serif;font-weight:600;font-size:13px;line-height:18px;color:var(--blue)}
.card-text{left:10px;width:156px;font-size:8.3px;line-height:18.4px;color:var(--grey);text-align:justify}

/* welcome band */
.band{left:0;top:930px;width:932px;height:210px;background:var(--blue-band)}
.band-title{font-family:'Signika',sans-serif;font-weight:600;font-size:19px;color:var(--white);display:flex;align-items:center;gap:10px}
.welcome-text{left:102px;width:450px;font-size:8.4px;line-height:17.5px;color:var(--white)}
.quote-box{left:578px;top:997px;width:253px;height:93px;background:var(--blue-box)}
.quote-box::after{content:"";position:absolute;left:50px;bottom:-7px;border:7px solid transparent;border-bottom:0;border-top-color:var(--blue-box)}
.quote-mark{left:12px;top:10px;font-family:'Signika',sans-serif;font-size:22px;color:var(--white);line-height:1}
.quote-text{left:31px;top:16px;width:208px;font-size:8.3px;line-height:17.5px;color:var(--white);text-align:justify}
.quote-author{left:618px;top:1107px;font-style:italic;font-size:8.5px;color:var(--white)}

/* footer */
.footer{left:0;top:1140px;width:932px;height:60px;background:var(--footer)}
.copyright{left:103px;top:1163px;font-size:9.5px;color:#ccc}
.social{top:1156px;width:26px;height:26px;border-radius:50%;border:1.5px solid #999}
</style>
</head>
<body>
  <div class="abs top-rule"></div>
  <header class="abs header"></header>
  <div class="abs brand">
    <div class="brand-mark"></div>
    <div class="brand-name">Marlowe Advisory</div>
  </div>
  <div class="abs phone">
    <svg width="20" height="20" viewBox="0 0 20 20"><circle cx="10" cy="10" r="9" fill="none" stroke="#3a8fd6" stroke-width="1.2"/><path d="M7 5.5c-.8.6-1.2 1.6-.8 2.8.8 2.4 2.6 4.4 5 5.3 1.1.4 2.1 0 2.7-.8l-1.6-1.6-1.2.7c-1.2-.6-2.1-1.6-2.6-2.8l.7-1.2z" fill="#3a8fd6"/></svg>
    0355 550 184
  </div>
  <nav class="abs nav">
    <a class="active" style="left:0;top:0">HOME</a>
    <a style="left:60px;top:0">ABOUT US</a>
    <a style="left:139px;top:0">SERVICES</a>
    <a style="left:212px;top:0">CONTACT US</a>
    <a style="left:302px;top:0">TESTIMONIALS</a>
  </nav>

  <section class="abs hero">
    <div class="abs hero-photo" role="img" aria-label="Photo of a consulting team gathered around a glossy meeting table in a dark office"></div>
    <div class="abs hero-text l1">NEW BUSINESS?</div>
    <div class="abs hero-text l2">GET THE KICK START</div>
    <div class="abs hero-text l3">YOU NEED!</div>
    <svg class="abs hero-arrow" style="left:26px" width="16" height="34" viewBox="0 0 16 34"><path d="M14 2L2 17l12 15" fill="none" stroke="#fff" stroke-width="1.5"/></svg>
    <svg class="abs hero-arrow" style="left:888px" width="16" height="34" viewBox="0 0 16 34"><path d="M2 2l12 15L2 32" fill="none" stroke="#fff" stroke-width="1.5"/></svg>
  </section>

  <h2 class="abs section-title">
    <svg width="26" height="26" viewBox="0 0 26 26"><circle cx="10" cy="16" r="7" fill="none" stroke="#c8c8c8" stroke-width="4" stroke-dasharray="3 2"/><circle cx="19" cy="7" r="4.5" fill="none" stroke="#c8c8c8" stroke-width="3" stroke-dasharray="2 1.5"/></svg>
    <div>OUR <span>SERVICES</span></div>
  </h2>

  <article class="abs card" style="left:102px">
    <div class="abs card-icon"><svg width="44" height="44" viewBox="0 0 44 44"><circle cx="22" cy="22" r="19" fill="none" stroke="#3a8fd6" stroke-width="2.5"/><rect x="14" y="22" width="4" height="8" fill="#3a8fd6"/><rect x="20" y="16" width="4" height="14" fill="#3a8fd6"/><rect x="26" y="20" width="4" height="10" fill="#3a8fd6"/></svg></div>
    <div class="abs card-photo" style="background:linear-gradient(135deg,#c9d4de,#6b7f94 60%,#2b3646)" role="img" aria-label="Photo of business people in a meeting reviewing reports"></div>
    <h3 class="abs card-title">BUSINESS ANALYSIS</h3>
    <p class="abs card-text" style="top:190px">Pinpoint critical goals and objectives to bring about maximum profitability and productivity through Marlowe's in depth and comprehensive business analysis reports.</p>
  </article>

  <article class="abs card" style="left:286px">
    <div class="abs card-icon"><svg width="44" height="44" viewBox="0 0 44 44"><circle cx="22" cy="22" r="19" fill="none" stroke="#3a8fd6" stroke-width="2.5"/><path d="M11 20l6-4 5 3 5-3 6 4-6 6-4-3-3 3z" fill="#3a8fd6"/></svg></div>
    <div class="abs card-photo" style="background:linear-gradient(135deg,#eef2f6,#b9c8d8 55%,#8fa6be)" role="img" aria-label="Photo of a coach presenting at a whiteboard to a seated team"></div>
    <h3 class="abs card-title">BUSINESS COACHING</h3>
    <p class="abs card-text" style="top:190px">Transfer essential business knowledge into your business, Brainstorm new and existing concepts, or develop and implement specific strategies via Marlowe's one...</p>
  </article>

  <article class="abs card" style="left:471px">
    <div class="abs card-icon"><svg width="44" height="44" viewBox="0 0 44 44"><circle cx="22" cy="22" r="19" fill="none" stroke="#3a8fd6" stroke-width="2.5"/><rect x="16" y="13" width="12" height="17" rx="1.5" fill="none" stroke="#3a8fd6" stroke-width="2"/><path d="M19 19h6M19 22.5h6M19 26h6" stroke="#3a8fd6" stroke-width="1.5"/></svg></div>
    <div class="abs card-photo" style="background:linear-gradient(135deg,#d9c3ad,#a88a70 55%,#6f5a4a)" role="img" aria-label="Photo of a smiling professional at a desk"></div>
    <h3 class="abs card-title">BUSINESS SYSTEM DESIGN AND DOCUMENT</h3>
    <p class="abs card-text" style="top:208px">Save time, money and free up valuable resources by outsourcing your business system or document creation projects to us.</p>
  </article>

  <article class="abs card" style="left:656px">
    <div class="abs card-icon"><svg width="44" height="44" viewBox="0 0 44 44"><circle cx="22" cy="22" r="19" fill="none" stroke="#3a8fd6" stroke-width="2.5"/><path d="M15 29l3-7 8-8c2-1 4-1 4-1s0 2-1 4l-8 8z" fill="none" stroke="#3a8fd6" stroke-width="1.8"/><circle cx="25" cy="19" r="1.6" fill="#3a8fd6"/></svg></div>
    <div class="abs card-photo" style="background:linear-gradient(135deg,#e4eaf0,#aebdcc 55%,#7c8fa3)" role="img" aria-label="Photo of a group of professionals around a conference table"></div>
    <h3 class="abs card-title" style="left:14px">NEW BUSINESS START-UP PACKAGES</h3>
    <p class="abs card-text" style="top:208px;left:14px;width:148px">Starting a new business? Marlowe provides simplistic, hassle free and easy to administer start-up packages that are a perfect...</p>
  </article>

  <section class="abs band"></section>
  <h2 class="abs band-title" style="left:102px;top:951px">
    <svg width="20" height="18" viewBox="0 0 20 18"><path d="M10 1L1 9h3v8h12V9h3z" fill="#5aa3e0"/></svg>
    WELCOME TO MARLOWE ADVISORY
  </h2>
  <div class="abs welcome-text" style="top:999px">
    <p>Marlowe Advisory is a business analysis, coaching and business development provider who specialises in assisting businesses to achieve maximum efficiency, increased productivity and who can assist with improving a business's overall profitability.</p>
    <p style="margin-top:10px">At Marlowe, we pride ourselves on our ability to form strong client relationships whilst delivering impressive results. For us, it's all about effective communication coupled with practical and measurable results!</p>
  </div>
  <h2 class="abs band-title" style="left:576px;top:951px">
    <svg width="20" height="18" viewBox="0 0 20 18"><rect x="1" y="2" width="12" height="9" rx="1.5" fill="#5aa3e0"/><rect x="7" y="7" width="12" height="9" rx="1.5" fill="#5aa3e0"/></svg>
    OUR TESTIMONIALS
  </h2>
  <svg class="abs" style="left:808px;top:957px" width="18" height="12" viewBox="0 0 18 12"><path d="M6 1L1 6l5 5" fill="none" stroke="#fff" stroke-width="1.6"/><path d="M12 1l5 5-5 5" fill="none" stroke="#6fb0e6" stroke-width="1.6"/></svg>
  <div class="abs quote-box">
    <div class="abs quote-mark">&ldquo;</div>
    <p class="abs quote-text">We envisage a simplistic design on this page with possibly a single image accompanied by some text that we can separate to depict the testimonials from each client We envisage</p>
  </div>
  <div class="abs quote-author">Dana Whitfield</div>

  <footer class="abs footer"></footer>
  <div class="abs copyright">&copy; Copy Rights 2014 - Marlowe Advisory . All rights reserved</div>
  <div class="abs social" style="left:718px" aria-label="Social link"></div>
  <div class="abs social" style="left:753px" aria-label="Social link"></div>
  <div class="abs social" style="left:792px" aria-label="Social link"></div>
</body>
</html>
```